"Fold The Map" A Song about getting better!

For my next Single i would like a cover around the concept "Fold the Map" meaning getting better than how you are now :)
I have attached the Picture and an idea for the title font. Mainly its the font that i would like you to design. It only has to be shaped like a stair but should be much more in shape and Color and has to fit in the Picture smoothly. There's also my artist logo which has to be attached to the cover :)
you are free to use colors, effects, filters or whatever your awesome creativity comes up with :P thanks! this is a great site!

Font styles to use
Decorative

Requirements
Must have
• designed and creative title font.

```html
<!DOCTYPE html>
<html lang="en">
<head>
<meta charset="utf-8">
<title>Fold The Map – Single Cover</title>
<link href="https://fonts.googleapis.com/css2?family=Silkscreen:wght@400;700&display=swap" rel="stylesheet">
<style>
  :root {
    --frame: #0e0e0e;
    --title-yellow: #f4dc1e;
    --title-shadow: #1b1b1b;
    --artist-ink: #1f3347;
    --sun: #f3ecc4;
    --moss: #9a9a58;
    --stone: #8a8784;
    --stone-dark: #55524f;
    --boot-teal: #4d6a74;
    --boot-purple: #8a5c93;
  }
  html, body {
    margin: 0;
    padding: 0;
    width: 1200px;
    height: 1200px;
    overflow: hidden;
    background: var(--frame);
  }
  .cover {
    position: relative;
    width: 1200px;
    height: 1200px;
    background: var(--frame);
    font-family: "Silkscreen", monospace;
  }
  .cover__photo {
    position: absolute;
    inset: 24px;
    background: linear-gradient(160deg,
      var(--sun) 0%,
      var(--moss) 22%,
      var(--boot-teal) 40%,
      var(--boot-purple) 55%,
      var(--stone) 70%,
      var(--stone-dark) 100%);
  }
  .artist-name {
    position: absolute;
    left: 78px;
    top: 80px;
    margin: 0;
    color: var(--artist-ink);
    font-weight: 700;
    font-size: 58px;
    line-height: 1.05;
  }
  .title {
    position: absolute;
    inset: 0;
    margin: 0;
    font-weight: 700;
    color: var(--title-yellow);
    text-shadow: 9px 9px 0 var(--title-shadow);
  }
  .title__step {
    position: absolute;
    font-size: 200px;
    line-height: 1;
  }
  .title__small {
    position: absolute;
    font-size: 62px;
    line-height: 1;
    text-shadow: 5px 5px 0 var(--title-shadow);
  }
</style>
</head>
<body>
  <main class="cover">
    <div class="cover__photo" role="img" aria-label="A worn child's boot in teal and purple leather with loose lilac laces, standing on a sunlit stone ledge with moss behind"></div>

    <p class="artist-name">Rowan<br>Velle</p>

    <h1 class="title" aria-label="Fold The Map">
      <span class="title__step" style="left:80px; top:880px;">F</span>
      <span class="title__step" style="left:190px; top:750px;">O</span>
      <span class="title__step" style="left:300px; top:620px;">L</span>
      <span class="title__step" style="left:410px; top:490px;">D</span>
      <span class="title__small" style="left:575px; top:400px;">T</span>
      <span class="title__small" style="left:575px; top:460px;">H</span>
      <span class="title__small" style="left:575px; top:520px;">E</span>
      <span class="title__step" style="left:640px; top:300px;">M</span>
      <span class="title__step" style="left:770px; top:170px;">A</span>
      <span class="title__step" style="left:890px; top:40px;">P</span>
    </h1>
  </main>
</body>
</html>
```